BVH Business Card Design

We are a small construction equipment rental and hardware store located in Middle Tennessee. We have three stores. Our primary business is construction equipment. We have an existing logo we'd like to use. I think I would like to list each store physical address on the back of the card and maybe the web address also: www.bvhhireyard.example.

We also need a design that we can incorporate into company letterhead, small note pads, and even checks if possible.

Industry/Entity Type

Construction

Contact Information for Business Card

We have our Logo, Name: Brookvale Hauling Machinery, Employee Name, Main Phone Number, Mobile Phone Number, Email Address, Company Address, and website information (There are three locations that can go on the back if necessary) We would like to leave some room on the back of the card in case we want to write information down on it.

```html
<!DOCTYPE html>
<html lang="en">
<head>
<meta charset="utf-8">
<title>BVH Business Card</title>
<link href="https://fonts.googleapis.com/css2?family=Open+Sans:wght@400;600;700;800&display=swap" rel="stylesheet">
<style>
  :root{
    --navy:#223a8c;
    --navy-deep:#1b2f78;
    --navy-light:#2d4aa3;
    --red:#e8314a;
    --grey:#8a8d94;
    --ink:#2b3566;
    --paper:#ffffff;
    --bg:#e9e7e3;
  }
  *{margin:0;padding:0;box-sizing:border-box}
  html,body{width:1200px;height:858px;overflow:hidden;background:var(--bg);font-family:"Open Sans",Arial,sans-serif}
  .canvas{position:relative;width:1200px;height:858px}
  .card{position:absolute;width:600px;height:343px;border-radius:3px;box-shadow:0 6px 18px rgba(0,0,0,.18);overflow:hidden}

  /* front */
  .card-front{left:120px;top:70px;background:var(--paper)}
  .brand{position:absolute;left:36px;top:112px;display:flex;align-items:center;gap:14px}
  .brand-mark{width:60px;height:60px;border-radius:50%;background:var(--navy);border:4px solid var(--red);flex:none}
  .brand-name{font-weight:800;font-size:15px;line-height:1.25;color:var(--grey);text-transform:uppercase;white-space:nowrap}
  .divider{position:absolute;left:330px;top:40px;width:1px;height:200px;background:var(--navy)}
  .contact{position:absolute;left:355px;top:52px}
  .city{font-size:30px;color:var(--red);font-weight:400;margin-bottom:14px}
  .contact-list{list-style:none}
  .contact-list li{display:flex;align-items:center;gap:10px;font-size:15px;color:var(--ink);line-height:27px;white-space:nowrap}
  .contact-list svg{width:15px;height:15px;flex:none}
  .address-band{position:absolute;left:0;bottom:0;width:100%;height:54px;background:var(--navy);color:#fff;font-size:17px;display:flex;align-items:center;padding-left:40px;white-space:nowrap}

  /* back */
  .card-back{left:480px;top:450px;background:linear-gradient(160deg,var(--navy-light),var(--navy-deep))}
  .back-name{position:absolute;left:44px;top:56px;color:#fff;font-weight:800;font-size:31px;line-height:1.15;text-transform:uppercase}
  .back-rule{position:absolute;left:0;right:0;top:238px;height:1px}
  .back-rule::before{content:"";position:absolute;left:0;width:30px;height:1px;background:#fff}
  .back-rule::after{content:"";position:absolute;left:270px;right:0;height:1px;background:#fff}
  .back-url{position:absolute;left:44px;top:227px;color:#fff;font-size:16px;white-space:nowrap}
</style>
</head>
<body>
<div class="canvas">
  <section class="card card-front">
    <div class="brand">
      <span class="brand-mark"></span>
      <span class="brand-name">Brookvale Hauling<br>Machinery</span>
    </div>
    <div class="divider"></div>
    <div class="contact">
      <div class="city">Brookvale</div>
      <ul class="contact-list">
        <li><svg viewBox="0 0 16 16"><rect x="3" y="1.5" width="10" height="13" rx="1.5" fill="none" stroke="var(--red)" stroke-width="1.6"/></svg>XXX XXX XXXX</li>
        <li><svg viewBox="0 0 16 16"><path d="M2 5c0-2 3-3 6-3s6 1 6 3v1h-3V5H5v1H2z M3 8h10v6H3z" fill="var(--red)"/></svg>XXX XXX XXXX</li>
        <li><svg viewBox="0 0 16 16"><circle cx="8" cy="8" r="7" fill="var(--red)"/><path d="M1 8h14M8 1c3 3 3 11 0 14M8 1c-3 3-3 11 0 14" stroke="#fff" stroke-width="1" fill="none"/></svg>www.bvhhireyard.example</li>
        <li><svg viewBox="0 0 16 16"><rect x="1" y="3" width="14" height="10" fill="var(--red)"/><path d="M1 3l7 6 7-6M1 13l5-5M15 13l-5-5" stroke="#fff" stroke-width="1.2" fill="none"/></svg>info@youremail.com</li>
      </ul>
    </div>
    <div class="address-band">Your Company Adress Inc 2nd Lane Ave Edison, NJ 00000</div>
  </section>

  <section class="card card-back">
    <div class="back-name">Brookvale Hauling<br>Machinery</div>
    <div class="back-rule"></div>
    <div class="back-url">www.bvhhireyard.example</div>
  </section>
</div>
</body>
</html>
```